Reworking our Ayurvedic Tea Boxes with Mordern and New look.

We are a Tea Wholesale company for retailers and health food stores. We have currently a Ayurvedic wellness tea line needs an updated packaging. We would like to see new modern, clean and beautiful new fresh look. Our current packaging can be seen at http://leafmerchantco.example/c/7720815/1/herbal-blends.html

We are going to launch various categories in the loose leaf tea line. This is just the first step. At present 9 different exsit in the wellnes line.
Updates

Target Market(s)

Health Food Stores, Specialty Food Stores, Grocery Stores.

Industry/Entity Type

It Company

Requirements
Must have
• - Name of the of the tea type should be clearly visible.
• - A modern fresh look. Not to heavy with design work.
Nice to have
• Box size is 8 cm (L) X 4.5 cm (W) X 15cm (H)

```html
<!DOCTYPE html>
<html lang="en">
<head>
<meta charset="utf-8">
<title>Ayurvedic Tea – Evening Time box dieline</title>
<link rel="stylesheet" href="https://fonts.googleapis.com/css2?family=Source+Sans+3:wght@300;400;600&display=swap">
<style>
  :root {
    --paper: #efe9df;
    --orange: #f7b56d;
    --brown: #5b3a18;
    --beige: #d2ccb2;
    --cream: #f4ead8;
    --cut: #8c7d6b;
    --white: #ffffff;
  }
  * { box-sizing: border-box; margin: 0; padding: 0; }
  html, body { width: 1200px; height: 1000px; overflow: hidden; }
  body {
    background: var(--paper);
    font-family: "Source Sans 3", "Myriad Pro", Arial, sans-serif;
    position: relative;
  }
  .dieline { position: absolute; inset: 0; }
  .cut-lines { position: absolute; inset: 0; }
  .panel { position: absolute; overflow: hidden; }
  .zone { position: absolute; left: 0; width: 100%; }
  .pattern { background: var(--orange); }
  .band { background: var(--brown); color: var(--white); }

  /* back panel */
  .panel-back { left: 190px; top: 200px; width: 320px; height: 600px; }
  .panel-back .pattern-top { top: 0; height: 180px; }
  .panel-back .band { top: 180px; height: 260px; padding: 26px 24px; }
  .panel-back .pattern-bottom { top: 440px; height: 160px; }
  .ingredients { font-size: 12.5px; line-height: 1.45; }
  .ingredients strong { font-weight: 600; }
  .net-weight { font-weight: 300; color: var(--cream); font-size: 15px; }
  .panel-back .net-weight { position: absolute; left: 24px; bottom: 24px; }

  /* side strip */
  .panel-side { left: 510px; top: 40px; width: 180px; height: 920px; background: var(--brown); color: var(--white); }
  .side-copy { position: absolute; top: 180px; left: 16px; right: 14px; }
  .tea-type { font-size: 17px; font-weight: 400; line-height: 1.1; }
  .tea-name { font-size: 22px; font-variant: small-caps; font-weight: 400; line-height: 1.15; margin-bottom: 12px; }
  .side-copy p { font-size: 11px; line-height: 1.45; margin-bottom: 12px; }

  /* front panel */
  .panel-front { left: 690px; top: 200px; width: 320px; height: 600px; }
  .panel-front .pattern-top { top: 0; height: 210px; }
  .panel-front .band { top: 210px; height: 230px; text-align: center; }
  .panel-front .pattern-bottom { top: 440px; height: 160px; }
  .label-box { position: absolute; top: 22px; left: 50px; width: 190px; }
  .label-title { background: var(--beige); color: var(--brown); text-align: center; padding: 10px 6px 8px; }
  .label-title .tea-type { font-size: 18px; }
  .label-title .tea-name { font-size: 27px; margin: 0; }
  .label-sub { background: var(--brown); color: var(--white); text-align: center; padding: 8px 6px 9px; margin-left: 12px; }
  .label-sub .caffeine { font-size: 13px; }
  .label-sub .format { font-size: 11px; font-variant: small-caps; margin-top: 6px; letter-spacing: .3px; }
  .brand { display: flex; align-items: center; justify-content: center; gap: 12px; padding-top: 62px; }
  .brand-dot { width: 18px; height: 18px; border-radius: 50%; background: var(--cream); }
  .brand-name { font-size: 38px; font-weight: 300; color: var(--cream); letter-spacing: 2px; }
  .panel-front .net-weight { margin-top: 40px; }
</style>
</head>
<body>
<main class="dieline" aria-label="Ayurvedic Tea Evening Time box dieline">

  <svg class="cut-lines" width="1200" height="1000" viewBox="0 0 1200 1000" aria-hidden="true">
    <g fill="none" stroke="var(--cut)" stroke-width="1">
      <path class="glue-tab" d="M190 215 L160 240 L160 760 L190 785"/>
      <path class="top-tuck" d="M510 40 L515 24 Q600 14 685 24 L690 40"/>
      <path class="bottom-tuck" d="M510 960 L515 976 Q600 986 685 976 L690 960"/>
      <path class="front-flap" d="M690 200 L700 180 L1000 180 L1010 200"/>
      <path class="back-flap" d="M190 800 L200 820 L500 820 L510 800"/>
    </g>
  </svg>

  <section class="panel panel-back" aria-label="Back panel">
    <div class="zone pattern pattern-top" role="img" aria-label="Scattered outline tea leaf pattern"></div>
    <div class="zone band">
      <p class="ingredients"><strong>INGREDIENTS:</strong> dolor sit amet, eos movet ultriam omittam te, ei illum partem dictas sit. Discere honestatis id per. Posse graeci quo no, suas inani quaerendum at sea. Ex mel nibh singulis. Eos eros oratio eu. Sit id doming appetere intellegat.</p>
      <p class="net-weight">Net weight: 3.5oz/<small>POIDS NET</small>:100gr</p>
    </div>
    <div class="zone pattern pattern-bottom" role="img" aria-label="Scattered outline tea leaf pattern"></div>
  </section>

  <section class="panel panel-side" aria-label="Side panel">
    <div class="side-copy">
      <p class="tea-type">Ayurvedic Tea</p>
      <p class="tea-name">Evening Time</p>
      <p>Lorem ipsum dolor sit amet, eos movet ultriam omittam te, ei illum partem dictas sit. Discere honestatis id per. Posse graeci quo no, suas inani quaerendum at sea. Ex mel nibh singulis. Eos eros oratio eu. Sit id doming appetere intellegat.</p>
      <p>Sed periculis signiferumque te, ne vero dolores detracto est. Etiam nostrum molestiae an his. Aeque ignota mei at. Pro utinam nominati ad, ex vix doctus splendide.</p>
      <p>Enim elit argumentum ex est. Vel ex stet iisque. Choro graece interpretaris ex pri, iriure equidem ullamcorper ad pro, quod legere mediocrem quo eu. No malestatis adversarium nam, eius quaerendum duo ut, ea alia oblique eligendi.</p>
    </div>
  </section>

  <section class="panel panel-front" aria-label="Front panel">
    <div class="zone pattern pattern-top" role="img" aria-label="Scattered outline tea leaf pattern"></div>
    <div class="label-box">
      <div class="label-title">
        <p class="tea-type">Ayurvedic Tea</p>
        <p class="tea-name">Evening Time</p>
      </div>
      <div class="label-sub">
        <p class="caffeine">Caffeine-Free/Sans Caféine</p>
        <p class="format">Loose Leaf Tea</p>
      </div>
    </div>
    <div class="zone band">
      <div class="brand">
        <span class="brand-dot"></span>
        <span class="brand-name">Leaf Merchant</span>
      </div>
      <p class="net-weight">Net weight: 3.5oz/<small>POIDS NET</small>:100gr</p>
    </div>
    <div class="zone pattern pattern-bottom" role="img" aria-label="Scattered outline tea leaf pattern"></div>
  </section>

</main>
</body>
</html>
```